New Website for Belcourt Manor at www.belcourt.com.au

A new logo has been designed (through pixel forge) and we now want to align the look and feel of our website at www.belcourt.com.au to the new logo. The content and page names (e.g. Grounds) will remain largely unchanged for the new site, so please submit a new look "Home" page, using our new logo, current text and any photos you choose from the existing gallery at our website. I have also attached the current "Home" page photos.

Industry/Entity Type

Accommodation

Number of Pages Required

1 page

Requirements
Must have
• Logo to be presented on white background.

```html
<!DOCTYPE html>
<html lang="en">
<head>
<meta charset="utf-8">
<title>Belcourt Manor – Palatial Estate and Luxury Resort</title>
<link href="https://fonts.googleapis.com/css2?family=Cinzel:wght@400;700&family=Lato:wght@400;700;900&family=Open+Sans:wght@400;600;700&display=swap" rel="stylesheet">
<style>
:root{
  --blue:#1f80c6;
  --blue-dark:#17609a;
  --blue-deep:#124c7c;
  --yellow:#f6c619;
  --text:#5a5a5a;
  --heading:#2a2a2a;
  --light:#eef3f8;
  --white:#ffffff;
}
*{box-sizing:border-box;margin:0;padding:0}
html,body{width:1200px;height:4724px;overflow:hidden}
body{font-family:"Open Sans",Arial,sans-serif;color:var(--text);background:var(--white);font-size:12px;line-height:1.5}
section,header,footer,nav{position:relative;width:1200px}
.abs{position:absolute}

/* header */
.site-header{height:110px;background:var(--white)}
.brand{left:180px;top:28px;display:flex;align-items:center;gap:10px}
.brand-dot{width:26px;height:26px;border-radius:50%;background:var(--yellow)}
.brand-name{font-family:"Lato",sans-serif;font-weight:700;font-size:30px;color:var(--blue)}
.header-contact{right:190px;top:24px;display:flex;align-items:center;gap:8px;font-weight:700;font-size:13px;color:var(--heading)}
.social-dot{width:14px;height:14px;border-radius:50%;background:var(--blue)}
.search{right:190px;top:55px;width:176px;height:26px;border:1px solid #ccc;font-size:11px;color:#999;padding:5px 8px}
.search svg{position:absolute;right:6px;top:6px}

.main-nav{height:35px;background:var(--blue);display:flex;justify-content:center;align-items:center;gap:22px}
.main-nav a{color:var(--white);text-decoration:none;font-family:"Lato",sans-serif;font-weight:700;font-size:12px;letter-spacing:.3px}

/* hero */
.hero{height:745px}
.hero-photo{position:absolute;inset:0;background:radial-gradient(ellipse at 50% 30%,#c4734a 0%,#8a6a45 18%,#3f5a32 45%,#24381f 100%)}
.hero-title{position:absolute;left:0;right:0;top:300px;text-align:center}
.hero-title h1{font-family:"Cinzel",serif;font-weight:400;font-size:46px;letter-spacing:5px;color:var(--white);display:inline-block;border-bottom:2px solid rgba(255,255,255,.7);padding:0 12px 6px}
.hero-title p{font-family:"Cinzel",serif;font-size:22px;letter-spacing:3px;color:var(--yellow);margin-top:10px}
.hero-arrow{left:588px;bottom:-12px;width:26px;height:26px;border-radius:50%;background:var(--blue);z-index:2}

/* booking */
.booking{height:118px;background:var(--blue)}
.field{position:absolute;top:42px}
.field label{display:block;color:var(--white);font-size:9px;text-transform:uppercase;margin-bottom:4px}
.field .box{height:28px;background:var(--white);font-size:10px;color:#444;padding:6px 8px;position:relative}
.btn-check{position:absolute;left:928px;top:58px;width:122px;height:28px;background:var(--yellow);color:var(--heading);font-weight:700;font-size:10px;text-align:center;line-height:28px;text-transform:uppercase}

/* headings */
.section-head{text-align:center;position:relative}
.section-head .ghost{font-family:"Lato",sans-serif;font-weight:900;font-size:90px;color:#f1f1f1;position:absolute;left:0;right:0;top:-20px;line-height:1}
.section-head h2{position:relative;font-family:"Lato",sans-serif;font-weight:900;font-size:18px;letter-spacing:2px;color:var(--heading)}
.section-head p{position:relative;max-width:520px;margin:40px auto 0;font-size:13px;color:var(--text)}

/* features */
.features{height:497px;padding-top:80px}
.feature{position:absolute;width:210px;display:flex;gap:10px}
.feature-img{flex:0 0 56px;height:56px;border-radius:50%;border:3px solid var(--light)}
.feature h3{font-family:"Lato",sans-serif;font-size:14px;font-weight:700;color:var(--heading)}
.feature p{font-size:10px;line-height:1.45}

/* property */
.property{height:635px;background:linear-gradient(180deg,#1f80c6 0%,#2a7fb4 50%,#1a6aa3 100%)}
.property-bg{position:absolute;inset:0;background:linear-gradient(160deg,rgba(31,128,198,.9),rgba(23,96,154,.85))}
.property-photo{left:173px;top:100px;width:332px;height:458px;background:linear-gradient(180deg,#efe3cc,#b58a5c 60%,#6d4a2c)}
.slider-arrow{position:absolute;top:50%;width:18px;height:28px;background:var(--blue);margin-top:-14px}
.property-body{left:540px;top:95px;width:480px;color:var(--white)}
.property-body h2{font-family:"Lato",sans-serif;font-weight:700;font-size:24px}
.property-body h2 span{color:var(--yellow)}
.property-body p{font-size:12px;margin:10px 0 14px}
.acc{height:34px;background:rgba(10,60,100,.45);display:flex;align-items:center;gap:10px;padding:0 14px;font-weight:700;font-size:13px;color:var(--white);margin-bottom:6px}
.tick{width:20px;height:20px;border-radius:50%;background:var(--yellow);display:flex;align-items:center;justify-content:center}
.acc-panel{background:var(--blue-deep);padding:12px 16px;display:grid;grid-template-columns:1fr 1fr;gap:8px 14px;margin-bottom:6px;font-size:11px}
.acc-panel div{display:flex;gap:8px;align-items:flex-start}
.acc-panel .tick{flex:0 0 14px;width:14px;height:14px}

/* gallery */
.gallery{height:1135px;padding-top:90px}
.filters{position:absolute;top:225px;left:0;right:0;display:flex;justify-content:center;gap:10px}
.filters span{background:var(--blue);color:var(--white);font-size:9px;font-weight:700;padding:5px 16px;text-transform:uppercase}
.thumb{position:absolute;width:265px;height:228px}
.btn-blue{position:absolute;background:var(--blue);color:var(--white);font-weight:700;font-size:11px;text-transform:uppercase;text-align:center}

/* location */
.location{height:347px;background:var(--blue)}
.location h2{left:180px;top:60px;font-family:"Lato",sans-serif;font-weight:700;font-size:22px;color:var(--white)}
.location h2 span{color:var(--yellow)}
.loc-item{position:absolute;display:flex;gap:12px;width:260px;color:var(--white);font-size:11px;line-height:1.3}
.loc-icon{flex:0 0 34px;height:34px;border-radius:50%;background:var(--blue-dark);display:flex;align-items:center;justify-content:center}
.loc-item b{color:var(--yellow);font-weight:700}
.map{left:772px;top:65px;width:246px;height:250px;background:linear-gradient(135deg,#e6ecef,#d3dde3)}

/* weddings */
.weddings{height:536px;padding-top:80px}
.wed-photo{left:173px;top:152px;width:332px;height:321px;background:linear-gradient(180deg,#c9d3d8,#9ea89a 55%,#5f6c4d)}
.wed-body{left:540px;top:148px;width:480px}
.wed-body h2{font-family:"Lato",sans-serif;font-weight:700;font-size:24px;color:var(--heading)}
.wed-body h2 span{color:var(--blue)}
.wed-body p{font-size:11px;margin-top:12px;line-height:1.55}

/* reviews & contact */
.connect{height:332px;background:var(--blue-dark)}
.connect h3{font-family:"Lato",sans-serif;font-weight:700;font-size:20px;color:var(--white)}
.connect h3 span{color:var(--yellow)}
.quote{left:180px;top:95px;width:390px;height:90px;background:var(--blue);color:var(--white);font-size:11px;text-align:center;padding:14px 22px}
.avatar{left:355px;top:190px;width:44px;height:44px;border-radius:50%;background:#d9c6b4;border:3px solid var(--white)}
.reviewer{left:180px;top:240px;width:390px;text-align:center;color:var(--white);font-size:11px}
.reviewer span{color:var(--yellow)}
.input{position:absolute;background:var(--white);font-size:10px;color:#999;padding:6px 10px}
.btn-submit{position:absolute;left:952px;top:255px;width:74px;height:26px;background:var(--yellow);color:var(--heading);font-weight:700;font-size:10px;text-align:center;line-height:26px;text-transform:uppercase}

/* footer info */
.footer-info{height:197px}
.info{position:absolute;top:40px;width:240px;text-align:center;font-size:10px}
.info-icon{width:50px;height:50px;margin:0 auto 10px;background:var(--blue);border-radius:8px;transform:rotate(45deg);display:flex;align-items:center;justify-content:center}
.info-icon svg{transform:rotate(-45deg)}
.info h4{font-weight:700;font-size:11px;color:var(--heading)}

.bottom-bar{height:37px;background:var(--blue-dark);color:var(--white);font-size:10px}
.bottom-bar .copy{left:180px;top:11px}
.bottom-bar .socials{right:180px;top:9px;display:flex;gap:6px}
.bottom-bar .socials i{width:18px;height:18px;border-radius:50%;background:var(--yellow);display:block}
</style>
</head>
<body>

<header class="site-header">
  <div class="abs brand"><span class="brand-dot"></span><span class="brand-name">Belcourt Manor</span></div>
  <div class="abs header-contact">
    <svg width="12" height="12" viewBox="0 0 24 24"><path fill="#1f80c6" d="M6.6 10.8a15 15 0 0 0 6.6 6.6l2.2-2.2c.3-.3.7-.4 1-.2 1.1.4 2.3.6 3.6.6.6 0 1 .4 1 1V20c0 .6-.4 1-1 1A17 17 0 0 1 3 4c0-.6.4-1 1-1h3.5c.6 0 1 .4 1 1 0 1.3.2 2.5.6 3.6.1.3 0 .7-.2 1z"/></svg>
    0400 123 456
    <span class="social-dot"></span><span class="social-dot"></span><span class="social-dot"></span>
  </div>
  <div class="abs search">Search...
    <svg width="12" height="12" viewBox="0 0 24 24"><circle cx="10" cy="10" r="6" fill="none" stroke="#555" stroke-width="2.5"/><path d="M15 15l6 6" stroke="#555" stroke-width="2.5"/></svg>
  </div>
</header>

<nav class="main-nav">
  <a>MAIN</a><a>MANSION</a><a>BEDROOMS</a><a>OPTIONS</a><a>COPPER KETTLE</a><a>GROUNDS</a><a>LOCATION</a><a>GALLERY</a><a>CONTACT</a><a>AVAILABILITY</a><a>DIY WEDDINGS</a>
</nav>

<section class="hero">
  <div class="hero-photo" role="img" aria-label="Aerial photo of the manor with red tiled roofs among palm trees"></div>
  <div class="hero-title">
    <h1>BELCOURT MANOR</h1>
    <p>PALATIAL ESTATE AND LUXURY RESORT</p>
  </div>
  <div class="abs hero-arrow"><svg width="26" height="26" viewBox="0 0 26 26"><path d="M8 15l5-5 5 5" fill="none" stroke="#fff" stroke-width="2"/></svg></div>
</section>

<section class="booking">
  <div class="field" style="left:173px;width:212px"><label>Select</label><div class="box">Belcourt Manor</div></div>
  <div class="field" style="left:394px;width:84px"><label>Check in date</label><div class="box">DD/MM/YY</div></div>
  <div class="field" style="left:504px;width:86px"><label>Check out date</label><div class="box">DD/MM/YY</div></div>
  <div class="field" style="left:614px;width:86px"><label>No. of rooms</label><div class="box">1</div></div>
  <div class="field" style="left:710px;width:100px"><label>Adults</label><div class="box">1</div></div>
  <div class="field" style="left:824px;width:90px"><label>Child</label><div class="box">1</div></div>
  <div class="btn-check">Check Availability</div>
</section>

<section class="features">
  <div class="section-head">
    <div class="ghost">B</div>
    <h2>BELCOURT FEATURES</h2>
    <p>Belcourt Manor is a unique coastal estate, centrally located in the prestigious rural suburb of Ashvale</p>
  </div>
  <div class="feature" style="left:173px;top:262px"><div class="feature-img" role="img" aria-label="Lounge photo" style="background:#b98e62"></div><div><h3>Lounge or Ballroom</h3><p>Stately lounge or ballroom with curved staircase and piano.</p></div></div>
  <div class="feature" style="left:394px;top:262px"><div class="feature-img" role="img" aria-label="Kitchen photo" style="background:#9b6b3f"></div><div><h3>Gourmet Kitchen</h3><p>New gourmet kitchen with stone benches and walk-in pantry.</p></div></div>
  <div class="feature" style="left:614px;top:262px"><div class="feature-img" role="img" aria-label="Bedroom photo" style="background:#c9a77f"></div><div><h3>Awesome Bedrooms</h3><p>All suites feature ensuites, walk-in robes, TVs and DVD players.</p></div></div>
  <div class="feature" style="left:835px;top:262px"><div class="feature-img" role="img" aria-label="Games room photo" style="background:#5b6f7a"></div><div><h3>Copper Kettle</h3><p>Big open room with pool table and entertainment system.</p></div></div>
  <div class="feature" style="left:173px;top:388px"><div class="feature-img" role="img" aria-label="Driveway photo" style="background:#7d8a5a"></div><div><h3>Circular Driveway</h3><p>Circular driveway with off-street parking for extra vehicles.</p></div></div>
  <div class="feature" style="left:394px;top:388px"><div class="feature-img" role="img" aria-label="Tennis court photo" style="background:#4e7d4a"></div><div><h3>Tennis Court</h3><p>Championship tennis court, synthetic grass with covered court house.</p></div></div>
  <div class="feature" style="left:614px;top:388px"><div class="feature-img" role="img" aria-label="Fountain photo" style="background:#8a8f7a"></div><div><h3>Stylish Fountain</h3><p>Garden courtyards and stylish fountain set amid lush palms.</p></div></div>
  <div class="feature" style="left:835px;top:388px"><div class="feature-img" role="img" aria-label="Pool photo" style="background:#3f8fb8"></div><div><h3>Saltwater Pool</h3><p>Large saltwater pool with lights and heated spa for guests.</p></div></div>
</section>

<section class="property">
  <div class="property-bg" role="img" aria-label="Faded aerial view of the estate in blue tones"></div>
  <div class="abs property-photo" role="img" aria-label="Bedroom with two beds and ceiling fan">
    <span class="slider-arrow" style="left:0"></span><span class="slider-arrow" style="right:0"></span>
  </div>
  <div class="abs property-body">
    <h2>Property <span>Descriptions</span></h2>
    <p>The estate features a grand mansion, private pub 'The Copper Kettle', sparkling saltwater pool, tennis court and playground. The open plan apartment contains a living room, dining area and kitchen – plus a large bedroom with king size bed, ensuite and walk-in robe. For special guests, this apartment is a fabulous haven in the heart of the estate.</p>
    <div class="acc"><span class="tick"><svg width="10" height="10" viewBox="0 0 10 10"><path d="M1 5l3 3 5-6" fill="none" stroke="#124c7c" stroke-width="1.8"/></svg></span>Mansion Features</div>
    <div class="acc"><span class="tick"><svg width="10" height="10" viewBox="0 0 10 10"><path d="M1 5l3 3 5-6" fill="none" stroke="#124c7c" stroke-width="1.8"/></svg></span>Copper Kettle Features</div>
    <div class="acc-panel">
      <div><span class="tick"></span>Wet bar with all the trimmings</div>
      <div><span class="tick"></span>Reverse cycle air-conditioning</div>
      <div><span class="tick"></span>Dining area or boardroom</div>
      <div><span class="tick"></span>Amazing lighting</div>
      <div><span class="tick"></span>Wood heater with pipe chimney</div>
      <div><span class="tick"></span>Big open room with pool table and entertainment system</div>
    </div>
    <div class="acc" style="margin-top:60px"><span class="tick"><svg width="10" height="10" viewBox="0 0 10 10"><path d="M1 5l3 3 5-6" fill="none" stroke="#124c7c" stroke-width="1.8"/></svg></span>Grounds Features</div>
  </div>
</section>

<section class="gallery">
  <div class="section-head">
    <div class="ghost">G</div>
    <h2>GALLERY</h2>
    <p>Magnificent properties rarely feel so warm and welcoming – so browse away and visit our photo gallery and we look forward to having you stay at our property.</p>
  </div>
  <div class="filters"><span>All</span><span>Mansion</span><span>Bedrooms</span><span>Copper Kettle</span><span>Grounds</span></div>
  <div class="thumb" role="img" aria-label="Manor lit at dusk" style="left:192px;top:280px;background:linear-gradient(180deg,#1c2a44,#6b5a3a)"></div>
  <div class="thumb" role="img" aria-label="Curved staircase" style="left:468px;top:280px;background:linear-gradient(180deg,#e8dcc6,#a77d52)"></div>
  <div class="thumb" role="img" aria-label="Lounge room" style="left:743px;top:280px;background:linear-gradient(180deg,#d7c7ad,#7a5637)"></div>
  <div class="thumb" role="img" aria-label="Dining room" style="left:192px;top:525px;background:linear-gradient(180deg,#e2d6c0,#6f4a2e)"></div>
  <div class="thumb" role="img" aria-label="Saltwater pool" style="left:468px;top:525px;background:linear-gradient(180deg,#6a8a5a,#2f86b5)"></div>
  <div class="thumb" role="img" aria-label="Living room with sofas" style="left:743px;top:525px;background:linear-gradient(180deg,#cdb79a,#5a3e2a)"></div>
  <div class="thumb" role="img" aria-label="Family room" style="left:192px;top:765px;background:linear-gradient(180deg,#e4ddd0,#8d6e4c)"></div>
  <div class="thumb" role="img" aria-label="Kitchen" style="left:468px;top:765px;background:linear-gradient(180deg,#d9c3a0,#8c5a2c)"></div>
  <div class="thumb" role="img" aria-label="Pool table room" style="left:743px;top:765px;background:linear-gradient(180deg,#c9a272,#2f5e86)"></div>
  <div class="btn-blue" style="left:510px;top:1050px;width:180px;height:40px;line-height:40px">View All Photos</div>
</section>

<section class="location">
  <h2 class="abs">Location - <span>24 Harrow Lane, Ashvale</span></h2>
  <div class="loc-item" style="left:190px;top:135px"><span class="loc-icon"><svg width="16" height="16" viewBox="0 0 24 24"><path d="M12 2a7 7 0 0 0-7 7c0 5 7 13 7 13s7-8 7-13a7 7 0 0 0-7-7z" fill="#fff"/></svg></span><div><b>Less than 2 minutes to</b><br>Ashvale Showground</div></div>
  <div class="loc-item" style="left:460px;top:135px"><span class="loc-icon"><svg width="16" height="16" viewBox="0 0 24 24"><path d="M12 2a7 7 0 0 0-7 7c0 5 7 13 7 13s7-8 7-13a7 7 0 0 0-7-7z" fill="#fff"/></svg></span><div><b>10 to 15 minutes to</b><br>Seabright</div></div>
  <div class="loc-item" style="left:190px;top:190px"><span class="loc-icon"><svg width="16" height="16" viewBox="0 0 24 24"><path d="M12 2a7 7 0 0 0-7 7c0 5 7 13 7 13s7-8 7-13a7 7 0 0 0-7-7z" fill="#fff"/></svg></span><div>Kelmont Town Centre<br><b>Less than 5 minutes to</b></div></div>
  <div class="loc-item" style="left:460px;top:190px"><span class="loc-icon"><svg width="16" height="16" viewBox="0 0 24 24"><path d="M12 2a7 7 0 0 0-7 7c0 5 7 13 7 13s7-8 7-13a7 7 0 0 0-7-7z" fill="#fff"/></svg></span><div>Marlow Heads<br><b>25 to 30 minutes to</b></div></div>
  <div class="loc-item" style="left:190px;top:245px"><span class="loc-icon"><svg width="16" height="16" viewBox="0 0 24 24"><path d="M12 2a7 7 0 0 0-7 7c0 5 7 13 7 13s7-8 7-13a7 7 0 0 0-7-7z" fill="#fff"/></svg></span><div>Kelmont Railway Station<br><b>Shopping outlets at Kelmont</b></div></div>
  <div class="loc-item" style="left:460px;top:245px"><span class="loc-icon"><svg width="16" height="16" viewBox="0 0 24 24"><path d="M12 2a7 7 0 0 0-7 7c0 5 7 13 7 13s7-8 7-13a7 7 0 0 0-7-7z" fill="#fff"/></svg></span><div>Harbourton<br><b>North and Kestrel Bay airport</b></div></div>
  <div class="abs map" role="img" aria-label="Street map showing the estate location"></div>
</section>

<section class="weddings">
  <div class="section-head">
    <div class="ghost">D</div>
    <h2>DIY WEDDINGS</h2>
  </div>
  <div class="abs wed-photo" role="img" aria-label="Wedding couple in front of the manor">
    <span class="slider-arrow" style="left:0"></span><span class="slider-arrow" style="right:0"></span>
  </div>
  <div class="abs wed-body">
    <h2>Do It Yourself Weddings at <span>Belcourt Manor</span></h2>
    <p>Properties such as Belcourt Manor are accommodation houses for short-term holidays – they are not licensed to operate as reception or function centres.</p>
    <p>If they were, you would not be talking to them about your DIY wedding. Instead, you would be discussing menus, drink packages, settings and other options.</p>
    <p>For many years, you could rent a property such as Belcourt Manor to hold your DIY wedding. However, in 2015, the local council introduced new regulations giving local councils the power to determine how to deal with the issue of "party houses", being short-term accommodation houses which operate as pseudo function centres. Designed to stop larger gatherings from being held at private residences, the council adopted these laws, which give them the power to identify party house restriction areas where residential properties are forbidden from operating.</p>
  </div>
  <div class="btn-blue" style="left:540px;top:425px;width:92px;height:30px;line-height:30px">Read More</div>
</section>

<section class="connect">
  <h3 class="abs" style="left:180px;top:45px">Guest <span>Reviews</span></h3>
  <div class="abs quote">Neque porro quisquam est, qui dolorem ipsum quia dolor sit amet, consectetur, adipisci velit, sed quia non numquam eius modi tempora incidunt ut labore et dolore magnam aliquam quaerat voluptatem.</div>
  <div class="abs avatar" role="img" aria-label="Guest portrait"></div>
  <div class="abs reviewer">Emily Hart<br><span>CEO</span>, Ashvale Events</div>
  <h3 class="abs" style="left:612px;top:45px">Quick <span>Contact</span></h3>
  <div class="input" style="left:612px;top:98px;width:200px;height:28px">Your name...</div>
  <div class="input" style="left:822px;top:98px;width:204px;height:28px">Your email...</div>
  <div class="input" style="left:612px;top:136px;width:414px;height:108px">Message...</div>
  <div class="btn-submit">Submit</div>
</section>

<section class="footer-info">
  <div class="info" style="left:200px">
    <div class="info-icon"><svg width="20" height="20" viewBox="0 0 24 24"><rect x="3" y="6" width="18" height="12" fill="none" stroke="#fff" stroke-width="2"/><path d="M3 6l9 7 9-7" fill="none" stroke="#fff" stroke-width="2"/></svg></div>
    <h4>Email Address :</h4>info@belcourt.com.au<br>bookings@belcourt.com.au
  </div>
  <div class="info" style="left:480px">
    <div class="info-icon"><svg width="20" height="20" viewBox="0 0 24 24"><path d="M12 2a7 7 0 0 0-7 7c0 5 7 13 7 13s7-8 7-13a7 7 0 0 0-7-7z" fill="#fff"/></svg></div>
    <h4>Street Location :</h4>24 Harrow Lane, Ashvale<br>Sunward Coast, Australia
  </div>
  <div class="info" style="left:760px">
    <div class="info-icon"><svg width="20" height="20" viewBox="0 0 24 24"><path fill="#fff" d="M6.6 10.8a15 15 0 0 0 6.6 6.6l2.2-2.2c.3-.3.7-.4 1-.2 1.1.4 2.3.6 3.6.6.6 0 1 .4 1 1V20c0 .6-.4 1-1 1A17 17 0 0 1 3 4c0-.6.4-1 1-1h3.5c.6 0 1 .4 1 1 0 1.3.2 2.5.6 3.6.1.3 0 .7-.2 1z"/></svg></div>
    <h4>Telephone :</h4>0400 123 456<br>0400 123 457
  </div>
</section>

<footer class="bottom-bar">
  <div class="abs copy">© Copyright information here</div>
  <div class="abs socials"><i></i><i></i><i></i></div>
</footer>

</body>
</html>
```